Norvale Structural Approval Standards Private Assessors

Professional Construction Consultancy Company Business Card - must keep logo colours see images below - examples have been added from my last competition - please see them as examples only!

Target Market(s)

Home Builders

Industry/Entity Type

Construction

Contact Information for Business Card

See "must haves"

Font styles to use
Sans Serif

Colors
ffffff
add136
000000

Requirements
Must have
• Daniel Moravi
• Director
• Phone: 0431 587 219
• Address: 7 Tarrunga Rd,
• Hallworth Vale, SA, 5091
• Email: norvaleassessors@mailbox-example.com
• Website: www.norvaleassessors-example.com.au
• Facebook: Norvale Structural Approval Standards
Nice to have
• Side 1: full logo
• Side 2: company details
Should not have
• hard to read
• must be clear and professional

```html
<!DOCTYPE html>
<html lang="en">
<head>
<meta charset="utf-8">
<title>Norvale Structural Approval Standards – Business Card</title>
<link rel="stylesheet" href="https://fonts.googleapis.com/css2?family=Source+Sans+3:wght@400;600;700&display=swap">
<style>
  :root {
    --backdrop: #4a2f1f;
    --card: #262626;
    --green: #add136;
    --white: #ffffff;
    --soft-white: #e8e8e8;
    --black: #000000;
  }
  * { margin: 0; padding: 0; box-sizing: border-box; }
  html, body {
    width: 1200px; height: 848px; overflow: hidden;
    background: var(--backdrop);
    font-family: "Source Sans 3", "Helvetica Neue", Arial, sans-serif;
  }
  .canvas { position: relative; width: 1200px; height: 848px; }
  .card {
    position: absolute; left: 270px; width: 658px; height: 353px;
    background: var(--card); border-radius: 22px;
    box-shadow: 0 4px 10px rgba(0,0,0,0.45);
    color: var(--white);
  }
  .card--front { top: 45px; }
  .card--back { top: 445px; }

  .brand-name {
    color: var(--green); font-weight: 700; text-transform: uppercase;
    line-height: 1.08; letter-spacing: 0.5px; white-space: nowrap;
  }
  .card--front .brand-name {
    position: absolute; left: 0; right: 0; top: 123px;
    text-align: center; font-size: 32px;
  }
  .website-line { font-size: 15px; color: var(--soft-white); }
  .website-line .accent { color: var(--green); }
  .card--front .website-line {
    position: absolute; left: 0; right: 0; top: 287px; text-align: center;
  }

  .card--back .brand-name {
    position: absolute; left: 26px; top: 139px; width: 280px;
    text-align: center; font-size: 22px;
  }
  .divider {
    position: absolute; left: 328px; top: 85px; width: 2px; height: 190px;
    background: linear-gradient(to bottom, rgba(173,209,54,0), var(--green) 50%, rgba(173,209,54,0));
  }
  .details { position: absolute; left: 362px; top: 81px; }
  .person-name { color: var(--green); font-size: 21px; font-weight: 400; line-height: 1.1; }
  .person-role { font-size: 15px; margin-top: 1px; line-height: 1.2; }
  .address { font-size: 14.5px; line-height: 19px; margin-top: 14px; color: var(--soft-white); }
  .contact-list { list-style: none; margin-top: 4px; }
  .contact-list li {
    display: flex; align-items: center; gap: 9px;
    font-size: 14.5px; height: 22.3px; color: var(--soft-white);
  }
  .contact-list .website-line { font-size: 14.5px; }
  .contact-list svg { width: 16px; height: 16px; flex: none; }
  .plain-dot { width: 14px; height: 14px; margin: 0 1px; border-radius: 50%; background: var(--green); flex: none; }
</style>
</head>
<body>
<div class="canvas">

  <section class="card card--front">
    <div class="brand-name">Norvale Structural<br>Approval Standards<br>Private Assessors</div>
    <div class="website-line">www.<span class="accent">norvaleassessors-example</span>.com.au</div>
  </section>

  <section class="card card--back">
    <div class="brand-name">Norvale Structural<br>Approval Standards<br>Private Assessors</div>
    <div class="divider"></div>
    <div class="details">
      <div class="person-name">Daniel Moravi</div>
      <div class="person-role">Director</div>
      <div class="address">7 Tarrunga Rd,<br>Hallworth Vale, SA, 5091</div>
      <ul class="contact-list">
        <li>
          <svg viewBox="0 0 16 16" aria-hidden="true"><path fill="#add136" d="M3.6 1.5l2.3 2.6-1.3 1.6c.9 2 2.6 3.7 4.6 4.6l1.6-1.3 2.6 2.3-1.4 2.2C7.3 13.3 2.7 8.7 2.5 3l1.1-1.5z"/></svg>
          0431 587 219
        </li>
        <li>
          <svg viewBox="0 0 16 16" aria-hidden="true"><rect x="1.5" y="4" width="13" height="8.5" fill="#add136"/><path d="M1.8 4.3L8 9l6.2-4.7" fill="none" stroke="#262626" stroke-width="1.2"/></svg>
          norvaleassessors@mailbox-example.com
        </li>
        <li>
          <svg viewBox="0 0 16 16" aria-hidden="true"><circle cx="8" cy="8" r="6.5" fill="none" stroke="#add136" stroke-width="1.5"/><ellipse cx="8" cy="8" rx="2.6" ry="6.5" fill="none" stroke="#add136" stroke-width="1.2"/><path d="M1.5 8h13" stroke="#add136" stroke-width="1.2"/></svg>
          <span class="website-line">www.<span class="accent">norvaleassessors-example</span>.com.au</span>
        </li>
        <li>
          <span class="plain-dot"></span>
          Norvale Structural Approval Standards
        </li>
      </ul>
    </div>
  </section>

</div>
</body>
</html>
```